BOLD & MINIMALIST DESIGN NEEDED

We want a very bold but minimalistic business card design that is impactful and utilizes both sides of the business card. Our current logo is included for your use.

We want bold fonts and good use of negative space. We don't want the logo to overpower the design.

Target Market(s)

Professionals who are building new commercial buildings.

Industry/Entity Type

Construction

Contact Information for Business Card

Name, Title, email, office phone, cell phone, website

Font styles to use
Serif
Sans Serif

Requirements
Must have
• Bold design!

```html
<!DOCTYPE html>
<html lang="en">
<head>
<meta charset="utf-8">
<title>Summitline Design + Build — Business Card</title>
<link rel="stylesheet" href="https://fonts.googleapis.com/css2?family=Montserrat:wght@400;500;600;800&display=swap">
<style>
  :root {
    --stage: #2e2e2e;
    --green: #86c440;
    --green-light: #cfe5a8;
    --ink: #111111;
    --paper: #ffffff;
    --muted: #1c1c1c;
  }
  * { box-sizing: border-box; margin: 0; padding: 0; }
  html, body { width: 1200px; height: 689px; overflow: hidden; }
  body {
    background: var(--stage);
    font-family: "Montserrat", sans-serif;
    position: relative;
  }
  .card {
    position: absolute;
    top: 190px;
    width: 540px;
    height: 309px;
    border-radius: 18px;
    overflow: hidden;
    box-shadow: 0 18px 40px rgba(0,0,0,.45);
  }
  .card--front {
    left: 40px;
    background: linear-gradient(90deg, var(--green-light) 0%, #a6d166 28%, var(--green) 100%);
    display: flex;
    align-items: center;
    justify-content: center;
  }
  .wordmark {
    text-align: center;
    font-weight: 800;
    color: var(--paper);
    line-height: 1;
  }
  .wordmark__name { font-size: 54px; letter-spacing: 1px; }
  .wordmark__tag { font-size: 22px; letter-spacing: 9px; margin-top: 10px; }
  .wordmark--dark { color: var(--ink); }
  .wordmark--dark .wordmark__name { font-size: 30px; letter-spacing: .5px; }
  .wordmark--dark .wordmark__tag { font-size: 12px; letter-spacing: 5px; margin-top: 6px; }

  .card--back { left: 620px; background: var(--paper); }
  .back__brand {
    position: absolute;
    left: 26px;
    top: 104px;
    width: 200px;
  }
  .back__divider {
    position: absolute;
    left: 240px;
    top: 52px;
    width: 2px;
    height: 150px;
    background: var(--green);
  }
  .contact {
    position: absolute;
    left: 262px;
    top: 44px;
    color: var(--muted);
  }
  .contact__name {
    color: var(--green);
    font-weight: 800;
    font-size: 26px;
    letter-spacing: .5px;
  }
  .contact__title { font-size: 14px; font-weight: 500; margin: 2px 0 12px; }
  .contact__list { list-style: none; }
  .contact__item {
    display: flex;
    align-items: center;
    gap: 10px;
    font-size: 14px;
    font-weight: 500;
    margin-bottom: 6px;
  }
  .contact__icon { width: 14px; height: 14px; fill: var(--green); flex: none; }
  .address {
    position: absolute;
    left: 26px;
    bottom: 46px;
    font-size: 13px;
    font-weight: 500;
    color: var(--muted);
  }
  .corner-band { position: absolute; right: 0; bottom: 0; }
</style>
</head>
<body>

<section class="card card--front" aria-label="Card front">
  <div class="wordmark">
    <div class="wordmark__name">SUMMITLINE</div>
    <div class="wordmark__tag">DESIGN + BUILD</div>
  </div>
</section>

<section class="card card--back" aria-label="Card back">
  <div class="back__brand wordmark wordmark--dark">
    <div class="wordmark__name">SUMMITLINE</div>
    <div class="wordmark__tag">DESIGN + BUILD</div>
  </div>

  <div class="back__divider"></div>

  <div class="contact">
    <h1 class="contact__name">MARCUS DALTON</h1>
    <p class="contact__title">Managing Director</p>
    <ul class="contact__list">
      <li class="contact__item">
        <svg class="contact__icon" viewBox="0 0 16 16" aria-hidden="true"><path d="M3 1l3 3-1.5 2a9 9 0 0 0 5.5 5.5L12 10l3 3-2 2C7 15 1 9 1 3z"/></svg>
        555-214-7730
      </li>
      <li class="contact__item">
        <svg class="contact__icon" viewBox="0 0 16 16" aria-hidden="true"><path d="M1 5c2-3 12-3 14 0l-2 2-2-1V4H5v2L3 7zM3 9h10l1 6H2z"/></svg>
        000 000 0000
      </li>
      <li class="contact__item">
        <svg class="contact__icon" viewBox="0 0 16 16" aria-hidden="true"><path d="M1 3h14v10H1zm1 1v1l6 4 6-4V4z"/></svg>
        info@yourmail.com
      </li>
      <li class="contact__item">
        <svg class="contact__icon" viewBox="0 0 16 16" aria-hidden="true"><circle cx="8" cy="8" r="7"/></svg>
        www.yourwebsite.com
      </li>
    </ul>
  </div>

  <p class="address">2400 Cedar Ridge Blvd, Ste 100, Dallas, TX 75204</p>

  <svg class="corner-band" width="540" height="309" viewBox="0 0 540 309" aria-hidden="true">
    <defs>
      <linearGradient id="bandFade" x1="0" x2="1" y1="0" y2="0">
        <stop offset="0" stop-color="#cfe5a8"/>
        <stop offset="1" stop-color="#86c440"/>
      </linearGradient>
    </defs>
    <polygon points="300,309 322,262 540,232 540,309" fill="url(#bandFade)"/>
    <polygon points="0,309 0,300 330,262 312,309" fill="#111111"/>
  </svg>
</section>

</body>
</html>
```